Mortgage Broking boutique Business

I’m wanting a revamped look to my existing business card design. I do like the black and silver but happy to have other colours introduced based on your creation. I’ve attached a copy of my current card so you can have a starting point updated details noted brloe. I deal with high net worth individuals so need my card to be sophisticated, classy that gives off a classy vibe

Target Market(s)

High net worth, wealthy

Industry/Entity Type

Mortgage Brokerage

Contact Information for Business Card

Job title: Finance Executive
Phone: +61 7 3287 4419
Mobile: 0471 352 608
Email: marcus@quillbrookcapital.com.au
Web: www.quillbrookcapital.com.au
Address: level 36 Tindale Court, 58 Harwick St Brisbane QLD 4000

Font styles to use
Other font styles liked:
• Helvetica

Colors

Designer to choose colors to be used in the design.

Requirements
Must have
• Use my existing card design as a starting point

```html
<!DOCTYPE html>
<html lang="en">
<head>
<meta charset="utf-8">
<title>Quillbrook Capital – Business Card</title>
<link rel="stylesheet" href="https://fonts.googleapis.com/css2?family=Jost:wght@400;500&family=Open+Sans:wght@300&family=Archivo+Black&family=PT+Sans+Narrow&display=swap">
<style>
  :root {
    --backdrop: #e6e4e1;
    --card-dark-top: #3a4045;
    --card-dark-mid: #1b1e21;
    --card-dark-bottom: #080808;
    --brand-silver: #c8c8c8;
    --card-light-top: #ffffff;
    --card-light-bottom: #eeeeee;
    --ink: #3b3f44;
    --ink-strong: #2b2e31;
    --icon-fill: #3b3f44;
    --icon-line: #ffffff;
    --divider: #dcdcdc;
  }
  * { margin: 0; padding: 0; box-sizing: border-box; }
  html, body {
    width: 1200px; height: 1200px; overflow: hidden;
    background: var(--backdrop);
  }
  .canvas { position: relative; width: 1200px; height: 1200px; }

  .card {
    position: absolute; left: 210px; width: 780px;
    box-shadow: 0 4px 14px rgba(0,0,0,0.18);
  }

  /* Front */
  .card-front {
    top: 140px; height: 443px;
    background: linear-gradient(180deg, var(--card-dark-top) 0%, var(--card-dark-mid) 45%, var(--card-dark-bottom) 100%);
    text-align: center;
    color: var(--brand-silver);
    font-family: "Jost", sans-serif;
  }
  .brand-name {
    position: absolute; left: 0; right: 0; top: 170px;
    font-size: 80px; font-weight: 500; letter-spacing: 4px; line-height: 1;
  }
  .brand-sub {
    position: absolute; left: 0; right: 0; top: 260px;
    font-size: 46px; font-weight: 400; letter-spacing: 5px; line-height: 1;
  }

  /* Back */
  .card-back {
    top: 648px; height: 444px;
    background: linear-gradient(160deg, var(--card-light-top) 0%, #f7f7f7 55%, var(--card-light-bottom) 100%);
    color: var(--ink);
  }
  .divider {
    position: absolute; left: 392px; top: 0; bottom: 0; width: 1px;
    background: linear-gradient(180deg, transparent, var(--divider) 30%, var(--divider) 70%, transparent);
  }
  .job-title { position: absolute; left: 22px; top: 176px; font-weight: normal; }
  .job-title-first {
    display: block;
    font-family: "Open Sans", sans-serif; font-weight: 300;
    font-size: 48px; line-height: 1; color: var(--ink-strong);
  }
  .job-title-second {
    display: block; margin: 10px 0 0 91px;
    font-family: "Archivo Black", sans-serif; font-weight: 400;
    font-size: 35px; line-height: 1; color: var(--ink-strong);
  }

  .contact-list { position: absolute; left: 450px; top: 100px; list-style: none; }
  .contact-item {
    position: absolute; left: 0; display: flex; align-items: center; gap: 12px;
    font-family: "PT Sans Narrow", sans-serif; font-size: 20px; color: var(--ink);
    white-space: nowrap;
  }
  .contact-item svg { width: 46px; height: 46px; flex: none; }
  .contact-email { top: 0; }
  .contact-phone { top: 62px; }
  .contact-mobile { top: 124px; }
  .contact-address { top: 186px; font-size: 17px; line-height: 1.35; }
  .contact-address span { text-align: center; }
  .contact-web { top: 254px; font-size: 19px; }
</style>
</head>
<body>
<main class="canvas">

  <section class="card card-front" aria-label="Business card front">
    <div class="brand-name">QUILLBROOK</div>
    <div class="brand-sub">CAPITAL</div>
  </section>

  <section class="card card-back" aria-label="Business card back">
    <div class="divider"></div>

    <h1 class="job-title">
      <span class="job-title-first">Finance</span>
      <span class="job-title-second">Executive</span>
    </h1>

    <ul class="contact-list">
      <li class="contact-item contact-email">
        <svg viewBox="0 0 46 46" aria-hidden="true">
          <circle cx="23" cy="23" r="23" fill="var(--icon-fill)"/>
          <rect x="12" y="15" width="22" height="15" fill="none" stroke="var(--icon-line)" stroke-width="2"/>
          <path d="M12 15 L23 24 L34 15" fill="none" stroke="var(--icon-line)" stroke-width="2"/>
        </svg>
        <span>marcus@quillbrookcapital.com.au</span>
      </li>
      <li class="contact-item contact-phone">
        <svg viewBox="0 0 46 46" aria-hidden="true">
          <circle cx="23" cy="23" r="23" fill="var(--icon-fill)"/>
          <path d="M16 12 c-3 1 -4 4 -3 7 c2 6 7 11 13 14 c3 1 6 0 7-3 l-5-4 l-3 2 c-3-1-6-4-7-7 l2-3 z" fill="var(--icon-line)"/>
        </svg>
        <span>+61 7 3287 4419</span>
      </li>
      <li class="contact-item contact-mobile">
        <svg viewBox="0 0 46 46" aria-hidden="true">
          <circle cx="23" cy="23" r="23" fill="var(--icon-fill)"/>
          <rect x="16" y="11" width="14" height="24" rx="2.5" fill="none" stroke="var(--icon-line)" stroke-width="2"/>
          <circle cx="23" cy="31" r="1.4" fill="var(--icon-line)"/>
        </svg>
        <span>0471 352 608</span>
      </li>
      <li class="contact-item contact-address">
        <svg viewBox="0 0 46 46" aria-hidden="true">
          <circle cx="23" cy="23" r="23" fill="var(--icon-fill)"/>
          <path d="M11 23 L23 12 L35 23 L32 23 L32 34 L26 34 L26 27 L20 27 L20 34 L14 34 L14 23 Z" fill="var(--icon-line)"/>
        </svg>
        <span>Level 36 Tindale Court, 58 Harwick<br>St Brisbane QLD 4000</span>
      </li>
      <li class="contact-item contact-web">
        <svg viewBox="0 0 46 46" aria-hidden="true">
          <circle cx="23" cy="23" r="23" fill="var(--icon-fill)"/>
          <circle cx="23" cy="23" r="10" fill="none" stroke="var(--icon-line)" stroke-width="2"/>
          <ellipse cx="23" cy="23" rx="4.5" ry="10" fill="none" stroke="var(--icon-line)" stroke-width="1.5"/>
          <line x1="13" y1="23" x2="33" y2="23" stroke="var(--icon-line)" stroke-width="1.5"/>
        </svg>
        <span>www.quillbrookcapital.com.au</span>
      </li>
    </ul>
  </section>

</main>
</body>
</html>
```